Swimming Pool Service business card needed!!!! Please

Hi Everyone! Thanks for looking at my contest. I PROMISE to provide excellent feedback during this process.

I am starting a new swimming pool cleaning business in San Diego, California and would like your help in making a business card for me.

I like easy to read, classy and sophisticated.

I am having a website designed and I'm looking for it to have pictures of really clean & clear pools.

I really like the blue on white color format, but open to other colors.

I do not have a logo, but the name of my company is GLIMMERTIDE POOL SERVICE.

My tag line is: Pools so clean, you can see yourself "in" them. (does not need to have the quotes around "in"...maybe just italics for this word IN?) You decide for me.

I would like to have a logo designed that incorporates some sort of easy to read letters. I do not want cursive (handwriting) letters. I thought about having a "reflection" of letters (mirror image), but think that this will be hard to read from far away. Maybe you can surprise me and come up with an idea that works using the a mirror image....but I'm not sure. I was leaning toward plain old BLOCK letters as I think it would be easy to read on my truck.

I would like to have the NAQTR and WBK logos on the back of the card. I have attached those two as files. You can put other things on the back as well, but I need these two logos on there. Or maybe put them on the front of the card if you have a better idea for the back of the card! :-)

Maybe blue on the back of the card and white on the front of the card? I don't know, I'm just thinking out loud.

I had another card done awhile ago called HARBORLINE TEES. I have uploaded a copy of that card for your reference. I don't want this card to be the same as my new company is a swimming pool cleaning company, but I wanted you to see what I liked in the past.

THANK YOU!!!!
Updates

Reason: Partner out of town and want their feedback....so need more time to decide and designs still coming in.

Industry/Entity Type

Business

Contact Information for Business Card

GLIMMERTIDE POOL SERVICE
Dale Wexby
Owner
4817 Quarry Bend Ave. #512
San Diego, CA 92417
858-291-6083
www.glimmertidepoolservice.example

Font styles to use
Sans Serif

Colors
0255a3
3176b5
ffffff

Requirements
Nice to have
• Some things to (possibly) add to back of card (in no particular order)
• WBK logo
• NAQTR logo
• Free Estimates
• Residential and Commercial Services
• Equipment Repairs
• Saltwater Systems
• Licensed, Bonded, Insured
• Family Owned and Operated
• No Contracts
• =======================
• Check out the FolioMint business card that i attached.
• i think they did this using a chrome overlay.
• Can any of you guys design that? or is that done at my printer?
• ==================
Should not have
• Hi Designers-
• The first round of cards came back and let's stay away from the light blue (powder blue) color. I don't like the look of it on the business cards.
• Also, the pool company JPG's that I attached are other logos of pool companies that I liked. I don't want them to be on my card. The only logos that should be on my card are the one you are going to come up with for my company, the WBK logo and the NAQTR logo.
• Lastly, no vertical cards and no split cards (logo on left, contact info on right side).
• Thanks much!

```html
<!DOCTYPE html>
<html lang="en">
<head>
<meta charset="utf-8">
<title>Glimmertide Pool Service – Business Card</title>
<link rel="stylesheet" href="https://fonts.googleapis.com/css2?family=Open+Sans:ital,wdth,wght@0,75..100,400;0,75..100,700;1,75..100,400&family=Questrial&display=swap">
<style>
  :root {
    --brand-blue: #0255a3;
    --mid-blue: #3176b5;
    --tagline-blue: #1a66b0;
    --paper: #ffffff;
    --ink: #1a1a1a;
    --edge: #9a9a9a;
    --canvas: #ffffff;
  }
  * { margin: 0; padding: 0; box-sizing: border-box; }
  html, body {
    width: 1200px; height: 708px; overflow: hidden;
    background: var(--canvas);
  }
  .stage { position: relative; width: 1200px; height: 708px; }

  .card {
    position: absolute;
    width: 630px; height: 371px;
    background: var(--paper);
    border: 1px solid var(--edge);
    border-radius: 14px;
    overflow: hidden;
    font-family: "Open Sans", Arial, sans-serif;
  }
  .card-band {
    position: absolute; left: 0; right: 0; bottom: 0;
    background: var(--brand-blue);
  }
  .wordmark {
    position: absolute;
    font-family: "Open Sans", Arial, sans-serif;
    font-weight: 700;
    font-stretch: 75%;
    color: var(--brand-blue);
    white-space: nowrap;
    letter-spacing: 0.2px;
  }
  .tagline {
    position: absolute;
    font-family: "Questrial", "Century Gothic", sans-serif;
    color: var(--tagline-blue);
    white-space: nowrap;
  }

  /* Back of card */
  .card-back { left: 567px; top: 0; z-index: 1; }
  .card-back .wordmark {
    left: 0; right: 0; top: 98px; text-align: center;
    font-size: 44px;
  }
  .card-back .tagline {
    left: 0; right: 0; top: 211px; text-align: center;
    font-size: 19.5px;
  }
  .card-back .card-band { height: 84px; }
  .service-list {
    position: absolute; left: 0; right: 0; top: 23px;
    text-align: center; color: var(--paper);
    font-size: 13px; line-height: 19.5px; white-space: nowrap;
  }
  .service-list span::before { content: "\2022\00a0"; }
  .service-list span { margin: 0 2px; }

  /* Front of card */
  .card-front { left: 1px; top: 336px; z-index: 2; }
  .card-front .wordmark {
    right: 38px; top: 30px; font-size: 21px;
  }
  .card-front .tagline {
    right: 36px; top: 83px; font-size: 11.5px;
  }
  .holder-name {
    position: absolute; left: 37px; top: 64px;
    font-size: 18px; font-weight: 700; color: var(--brand-blue);
  }
  .holder-role {
    position: absolute; left: 50px; top: 88px;
    font-size: 13px; font-style: italic; color: var(--mid-blue);
  }
  .address {
    position: absolute; left: 41px; top: 135px;
    font-size: 14px; line-height: 19.5px; color: var(--ink);
    font-style: normal;
  }
  .contact {
    position: absolute; left: 37px; font-size: 14px; color: var(--ink);
  }
  .contact b { color: var(--brand-blue); font-size: 15px; }
  .contact-phone { top: 210px; }
  .contact-web { top: 235px; }
  .card-front .card-band { height: 82px; }
  .badges {
    position: absolute; right: 30px; top: 10px;
    display: flex; gap: 16px;
  }
  .badge { width: 63px; height: 63px; background: var(--paper); display: block; }
</style>
</head>
<body>
<main class="stage">

  <section class="card card-back" aria-label="Back of business card">
    <div class="wordmark">GLIMMERTIDE POOL SERVICE</div>
    <p class="tagline">Pools so clean, you can see yourself <em>in</em> them.</p>
    <div class="card-band">
      <p class="service-list">
        <span>Free Estimates</span><span>Residential and Commercial Services</span><span>Equipment Repairs</span><br>
        <span>Saltwater Systems</span><span>Licensed, Bonded, Insured</span><span>Family Owned and Operated</span><span>No Contracts</span>
      </p>
    </div>
  </section>

  <section class="card card-front" aria-label="Front of business card">
    <div class="wordmark">GLIMMERTIDE POOL SERVICE</div>
    <p class="tagline">Pools so clean, you can see yourself <em>in</em> them.</p>

    <h1 class="holder-name">Dale Wexby</h1>
    <p class="holder-role">Owner</p>

    <address class="address">
      4817 Quarry Bend Ave.<br>
      #512 San Diego,<br>
      CA 92417
    </address>

    <p class="contact contact-phone"><b>Phone:</b> 858-291-6083</p>
    <p class="contact contact-web"><b>Website:</b> www.glimmertidepoolservice.example</p>

    <div class="card-band">
      <div class="badges">
        <svg class="badge" viewBox="0 0 63 63" role="img" aria-label="NAQTR membership badge">
          <rect width="63" height="63" fill="#ffffff"/>
        </svg>
        <svg class="badge" viewBox="0 0 63 63" role="img" aria-label="WBK certification badge">
          <rect width="63" height="63" fill="#ffffff"/>
        </svg>
      </div>
    </div>
  </section>

</main>
</body>
</html>
```